Silver Heron Construction Services

Create a business card for my business consulting company
Danielle Vesk, Founder and CEO
4816 Alder Brook Way, Ste 100
Denver, CO. 80451
303.782.4190 cell
dvesk@silverheronconst.example
www.silverheronconst.example

Target Market(s)

Private Equity and Construction Companies

Industry/Entity Type

Business / Sales Consulting

Contact Information for Business Card

Tag Line that says "Where The Road To Success Is Always Under Construction"

Requirements
Must have
• Logo on both sides of the card.
Nice to have
• Add tagline to the same side of the card as my name and contact info

```html
<!DOCTYPE html>
<html lang="en">
<head>
<meta charset="utf-8">
<title>Silver Heron Construction Services – Business Card</title>
<link href="https://fonts.googleapis.com/css2?family=Montserrat:wght@500;600;700&display=swap" rel="stylesheet">
<style>
  :root {
    --page-bg: #e9e9e9;
    --card-bg: #ffffff;
    --ink: #111111;
    --ink-soft: #1c1c1c;
  }
  * { box-sizing: border-box; margin: 0; padding: 0; }
  html, body {
    width: 695px;
    height: 1200px;
    overflow: hidden;
    background: var(--page-bg);
    font-family: "Montserrat", sans-serif;
    color: var(--ink);
  }
  .sheet {
    position: relative;
    width: 695px;
    height: 1200px;
  }
  .card {
    position: absolute;
    left: 47px;
    width: 600px;
    height: 345px;
    background: var(--card-bg);
    box-shadow: 0 2px 10px rgba(0,0,0,0.08);
  }
  .card--front { top: 170px; }
  .card--back { top: 650px; }

  /* Wordmark */
  .wordmark {
    position: absolute;
    display: flex;
    align-items: center;
    color: var(--ink);
    font-weight: 700;
    text-transform: uppercase;
  }
  .wordmark__square {
    flex: none;
    background: var(--ink);
  }
  .wordmark__text { line-height: 1.2; }

  .card--front .wordmark {
    left: 0; right: 0; top: 0; bottom: 0;
    justify-content: center;
    gap: 14px;
    font-size: 19px;
    letter-spacing: 0.5px;
  }
  .card--front .wordmark__square { width: 22px; height: 22px; }
  .card--front .wordmark__text { text-align: left; }

  .card--back .wordmark {
    left: 24px;
    top: 52px;
    gap: 9px;
    font-size: 10.5px;
    letter-spacing: 0.3px;
  }
  .card--back .wordmark__square { width: 14px; height: 14px; }

  /* Identity */
  .identity {
    position: absolute;
    right: 24px;
    top: 26px;
    text-align: right;
  }
  .identity__name {
    font-size: 26px;
    font-weight: 700;
    letter-spacing: 0.2px;
    color: var(--ink-soft);
  }
  .identity__title {
    margin-top: 3px;
    font-size: 15px;
    font-weight: 500;
  }

  /* Contact */
  .contact {
    position: absolute;
    right: 24px;
    top: 140px;
    list-style: none;
    font-size: 15.5px;
    font-weight: 500;
  }
  .contact__item {
    display: flex;
    justify-content: flex-end;
    align-items: flex-start;
    gap: 12px;
    margin-bottom: 5px;
    text-align: right;
    line-height: 20px;
  }
  .contact__item--phone { letter-spacing: 1.5px; }
  .contact__icon {
    flex: none;
    width: 8px;
    height: 20px;
  }

  /* Tagline */
  .tagline {
    position: absolute;
    left: 24px;
    right: 24px;
    bottom: 26px;
    font-size: 13.5px;
    font-weight: 700;
    letter-spacing: 2.55px;
    white-space: nowrap;
    text-align: right;
  }
</style>
</head>
<body>
<main class="sheet">

  <section class="card card--front" aria-label="Card front">
    <div class="wordmark">
      <span class="wordmark__square" aria-hidden="true"></span>
      <span class="wordmark__text">Silver Heron<br>Construction Services</span>
    </div>
  </section>

  <section class="card card--back" aria-label="Card back">
    <div class="wordmark">
      <span class="wordmark__square" aria-hidden="true"></span>
      <span class="wordmark__text">Silver Heron<br>Construction Services</span>
    </div>

    <header class="identity">
      <h1 class="identity__name">Danielle Vesk</h1>
      <p class="identity__title">Founder and CEO</p>
    </header>

    <ul class="contact">
      <li class="contact__item contact__item--phone">
        <span>303.782.4190</span>
        <svg class="contact__icon" viewBox="0 0 8 20" aria-hidden="true">
          <rect x="1" y="5" width="6" height="10" rx="1" fill="none" stroke="#111" stroke-width="1.2"/>
        </svg>
      </li>
      <li class="contact__item">
        <span>dvesk@silverheronconst.example</span>
        <svg class="contact__icon" viewBox="0 0 8 20" aria-hidden="true">
          <circle cx="4" cy="11" r="2.8" fill="#111"/>
        </svg>
      </li>
      <li class="contact__item">
        <span>4816 Alder Brook Way, Ste 100<br>Denver, CO. 80451</span>
        <svg class="contact__icon" viewBox="0 0 8 20" aria-hidden="true">
          <circle cx="4" cy="8" r="2" fill="none" stroke="#111" stroke-width="1.2"/>
          <path d="M1 14 H7" stroke="#111" stroke-width="1.4"/>
        </svg>
      </li>
    </ul>

    <p class="tagline">The Road To Success Is Always Under Construction</p>
  </section>

</main>
</body>
</html>
```